Beacon Advisory Website

I currently have a website www.beaconadvisoryinc.example. We are a IT Consulting Company. Our website will pretty much tell out our services. I am looking to enhance my website and make it look more professional. Looking for very classy and Contemporary look and design for my website.

Industry/Entity Type

It Company

```html
<!DOCTYPE html>
<html lang="en">
<head>
<meta charset="utf-8">
<title>Beacon Advisory</title>
<link rel="stylesheet" href="https://fonts.googleapis.com/css2?family=Roboto:wght@300;400;500;700&display=swap">
<style>
:root{
  --navy:#0b3a86;
  --brand:#1f4f9c;
  --sky:#0296d6;
  --sky-dark:#0584c2;
  --sky-light:#12a6e3;
  --ink:#1d1d1d;
  --grey:#6b6b6b;
  --footer:#1c1c1c;
  --footer-line:#3a3a3a;
  --copyright:#0c2148;
  --accent:#2aa7e3;
}
*{margin:0;padding:0;box-sizing:border-box}
html,body{width:1200px;height:2799px;overflow:hidden}
body{position:relative;font-family:'Roboto',Arial,sans-serif;background:#fff;color:var(--ink)}
.abs{position:absolute}

/* header */
.site-header{left:0;top:0;width:1200px;height:88px;background:#fff;border-top:3px solid var(--navy)}
.brand{left:80px;top:14px;display:flex;align-items:center;gap:10px}
.brand-mark{width:56px;height:56px;border-radius:50%;background:var(--brand)}
.brand-name{font-size:26px;font-weight:700;color:var(--brand);letter-spacing:.5px;line-height:1}
.main-nav{right:80px;top:35px;display:flex;gap:28px;font-size:14.5px;color:#222}
.main-nav .active{color:var(--brand)}

/* hero */
.hero{left:0;top:88px;width:1200px;height:580px;background:linear-gradient(90deg,#8d8f96 0%,#b9b7b3 35%,#d4cdc4 55%,#a9a7a8 75%,#6f7076 100%)}
.hero-tag{left:0;top:350px;width:540px;height:100px;background:rgba(255,255,255,.78);padding:14px 0 0 80px}
.hero-tag p{font-size:35px;color:var(--brand);line-height:41px;font-weight:400}

/* welcome */
.section-title{width:1200px;text-align:center;font-size:31px;font-weight:400;color:#111}
.section-title span{color:var(--brand)}
.welcome-text{left:88px;width:1024px;text-align:center;font-size:13.5px;line-height:26px;color:var(--grey)}
.globe-art{left:230px;top:920px;width:740px;height:268px;background:radial-gradient(ellipse at 50% 30%,#3c7fc0 0 9%,#e9edf2 10%,#f7f8fa 70%,#ffffff 100%)}

/* services */
.services{left:0;top:1188px;width:1200px;height:770px;background:var(--sky)}
.services svg.bg{position:absolute;left:0;top:0}
.services .section-title{color:#fff;top:75px}
.service{width:372px;text-align:center;color:#fff}
.service-icon{width:96px;height:96px;border-radius:50%;background:#fff;border:4px solid #0c2a55;margin:0 auto;display:flex;align-items:center;justify-content:center}
.service h3{font-size:20px;font-weight:400;color:#0d1b33;margin-top:34px;letter-spacing:.3px}
.service p{font-size:12.5px;line-height:21px;margin:10px auto 0;width:300px;font-weight:500}

/* clients */
.clients-text{left:100px;width:1000px;text-align:center;font-size:13.5px;line-height:26px;color:var(--grey)}
.slider-arrow{width:50px;height:50px;border-radius:50%;background:#a7a7a7}
.client-strip{left:160px;top:2226px;width:880px;height:72px;display:flex;align-items:center}
.client{flex:1;height:72px;display:flex;align-items:center;justify-content:center;gap:8px;font-size:21px;color:#333;border-right:1px solid #cfcfcf}
.client:last-child{border-right:0}
.client i{width:12px;height:12px;border-radius:50%;background:#e35a20;display:block}

/* why */
.why{left:0;top:2352px;width:1200px;height:125px;background:linear-gradient(90deg,#0a2f74,#0d3c92)}
.why h2{left:80px;top:42px;font-size:31px;font-weight:400;color:#fff}
.why p{left:435px;top:24px;width:690px;font-size:13px;line-height:26px;color:#a9c1e6}

/* footer */
.site-footer{left:0;top:2477px;width:1200px;height:275px;background:var(--footer);color:#ddd}
.f-col h4{font-size:15px;font-weight:700;color:var(--accent);padding-bottom:6px;border-bottom:1px solid var(--footer-line)}
.f-col ul{list-style:none;margin-top:10px}
.quick li{font-size:13px;line-height:21.5px;padding-left:10px;position:relative}
.quick li:before{content:"";position:absolute;left:0;top:8px;border-left:4px solid #ddd;border-top:3px solid transparent;border-bottom:3px solid transparent}
.contact li{font-size:13px;line-height:18px;display:flex;gap:12px;margin-bottom:10px}
.contact svg{flex:none;margin-top:2px}
.newsletter p{font-size:11px;line-height:17px;margin-top:10px}
.newsletter .email-box{width:203px;height:25px;background:#fff;margin-top:8px;font-size:11px;color:#555;padding:5px 7px}
.newsletter .subscribe{display:inline-block;margin-top:8px;background:var(--accent);color:#fff;font-size:11px;padding:5px 8px}
.social li{display:flex;align-items:center;gap:12px;font-size:13px;margin-bottom:10px}
.social i{width:24px;height:24px;display:block;border-radius:3px}
.copyright{left:0;top:2752px;width:1200px;height:47px;background:var(--copyright);text-align:center;font-size:11px;line-height:47px;color:#7f8fb0}
</style>
</head>
<body>

<header class="site-header abs">
  <div class="brand abs"><span class="brand-mark"></span><span class="brand-name">BEACON<br><span style="font-size:13px;font-weight:400;letter-spacing:2px">ADVISORY</span></span></div>
  <nav class="main-nav abs">
    <span class="active">HOME</span><span>SERVICES</span><span>SOLUTIONS</span><span>RESOURCES</span><span>CAREER</span><span>CONTACT US</span>
  </nav>
</header>

<section class="hero abs" role="img" aria-label="Photo of a smiling consultant holding folders in front of a team of business people in an office"></section>
<div class="hero-tag abs"><p>WE CREATE EXPERIENCE.<br>WE DELIVER RESULTS.</p></div>

<h2 class="section-title abs" style="top:722px">WELCOME TO <span>BEACON ADVISORY</span></h2>
<p class="welcome-text abs" style="top:803px">Today's IT market is a dynamic, fast-paced industry, with ever-increasing demands. Meeting these demands for over 25 years, Beacon Advisory maintains a global presence, aggressively recruiting expertly qualified IT and Management Professionals from around the world and cultivating key partnerships with corporations to understand their business models end-to-end, with a goal of delivering exceptional client service and ensuring a consistent delivery of the talent needed to drive results.</p>
<div class="globe-art abs" role="img" aria-label="Illustration of business people silhouettes standing around a blue globe on a reflective floor"></div>

<section class="services abs">
  <svg class="bg" width="1200" height="770" viewBox="0 0 1200 770">
    <polygon points="0,0 600,0 0,400" fill="var(--sky-light)"/>
    <polygon points="600,0 1200,0 1200,400" fill="var(--sky-light)" opacity=".5"/>
    <polygon points="0,770 0,330 640,770" fill="var(--sky-dark)"/>
    <polygon points="1200,770 1200,120 420,770" fill="var(--sky-dark)" opacity=".8"/>
  </svg>
  <h2 class="section-title abs">SERVICES</h2>

  <div class="service abs" style="left:42px;top:140px">
    <div class="service-icon"><svg width="50" height="50" viewBox="0 0 50 50" fill="none" stroke="#0c3f8a" stroke-width="4"><circle cx="18" cy="30" r="9"/><circle cx="35" cy="15" r="6"/><circle cx="36" cy="38" r="5"/></svg></div>
    <h3>TECHNOLOGY</h3>
    <p>Lorem Ipsum is simply dummy text of the printing and typesetting industry. Lorem Ipsum has been the industry's standard dummy text ever since the 1500s, when an unknown printer .</p>
  </div>
  <div class="service abs" style="left:414px;top:140px">
    <div class="service-icon"><svg width="50" height="50" viewBox="0 0 50 50" fill="#0c3f8a"><rect x="8" y="32" width="6" height="10"/><rect x="18" y="26" width="6" height="16"/><rect x="28" y="30" width="6" height="12"/><rect x="38" y="20" width="6" height="22"/><polyline points="6,28 18,18 28,24 44,8" fill="none" stroke="#0c3f8a" stroke-width="3"/></svg></div>
    <h3>BUSINESS</h3>
    <p>Lorem Ipsum is simply dummy text of the printing and typesetting industry. Lorem Ipsum has been the industry's standard dummy text ever since the 1500s, when an unknown printer .</p>
  </div>
  <div class="service abs" style="left:786px;top:140px">
    <div class="service-icon"><svg width="50" height="50" viewBox="0 0 50 50" fill="none" stroke="#0c3f8a" stroke-width="3"><rect x="14" y="8" width="28" height="22"/><rect x="8" y="18" width="28" height="24" fill="#fff"/><line x1="8" y1="24" x2="36" y2="24"/></svg></div>
    <h3>APPLICATION DEVELOPEMENT</h3>
    <p>Lorem Ipsum is simply dummy text of the printing and typesetting industry. Lorem Ipsum has been the industry's standard dummy text ever since the 1500s, when an unknown printer .</p>
  </div>

  <div class="service abs" style="left:42px;top:455px">
    <div class="service-icon"><svg width="50" height="50" viewBox="0 0 50 50" fill="#0c3f8a"><ellipse cx="16" cy="16" rx="8" ry="3"/><ellipse cx="16" cy="23" rx="8" ry="3"/><ellipse cx="34" cy="16" rx="8" ry="3"/><ellipse cx="34" cy="23" rx="8" ry="3"/><ellipse cx="25" cy="30" rx="8" ry="3"/><ellipse cx="25" cy="37" rx="8" ry="3"/></svg></div>
    <h3>ENTERPRISE INTEGRATION</h3>
    <p>Lorem Ipsum is simply dummy text of the printing and typesetting industry. Lorem Ipsum has been the industry's standard dummy text ever since the 1500s, when an unknown printer .</p>
  </div>
  <div class="service abs" style="left:414px;top:455px">
    <div class="service-icon"><svg width="50" height="50" viewBox="0 0 50 50" fill="#0c3f8a"><rect x="10" y="12" width="30" height="18" fill="none" stroke="#0c3f8a" stroke-width="3"/><rect x="6" y="34" width="38" height="4"/><rect x="12" y="38" width="3" height="6"/><rect x="35" y="38" width="3" height="6"/></svg></div>
    <h3>IT CONSULTING</h3>
    <p>Lorem Ipsum is simply dummy text of the printing and typesetting industry. Lorem Ipsum has been the industry's standard dummy text ever since the 1500s, when an unknown printer .</p>
  </div>
  <div class="service abs" style="left:786px;top:455px">
    <div class="service-icon"><svg width="50" height="50" viewBox="0 0 50 50" fill="none" stroke="#0c3f8a" stroke-width="4"><path d="M12 20 A14 14 0 0 1 36 14"/><path d="M38 30 A14 14 0 0 1 14 36"/><polyline points="32,8 37,15 30,18" /><polyline points="18,42 13,35 20,32"/></svg></div>
    <h3>CLEAN PROCESS</h3>
    <p>Lorem Ipsum is simply dummy text of the printing and typesetting industry. Lorem Ipsum has been the industry's standard dummy text ever since the 1500s, when an unknown printer .</p>
  </div>
</section>

<h2 class="section-title abs" style="top:2010px">WE ARE TRUSTED BY <span>COOL COMANIES</span></h2>
<p class="clients-text abs" style="top:2092px">Contrary to popular belief, Lorem Ipsum is not simply random text. It has roots in a piece of classical Latin literature from 45 BC, making it over 2000 years old. Rupert Marlowe, a Latin professor at Ashford Hill College in Vermont, looked up one of the more obscure Latin words, consectetur, from a Lorem Ipsum passage, and going through the cites of the word in classical literature, discovered the undoubtable source.</p>

<div class="slider-arrow abs" style="left:78px;top:2237px"><svg width="50" height="50" viewBox="0 0 50 50"><polyline points="28,17 20,25 28,33" fill="none" stroke="#fff" stroke-width="3"/></svg></div>
<div class="client-strip abs">
  <div class="client"><i></i>Northwind Co</div>
  <div class="client">Stonecraft</div>
  <div class="client">Halden Capital</div>
  <div class="client">Brightleaf</div>
  <div class="client">Vertex Works</div>
</div>
<div class="slider-arrow abs" style="left:1069px;top:2237px"><svg width="50" height="50" viewBox="0 0 50 50"><polyline points="22,17 30,25 22,33" fill="none" stroke="#fff" stroke-width="3"/></svg></div>

<section class="why abs">
  <svg class="abs" style="left:0;top:0" width="420" height="125"><polygon points="0,0 310,0 410,125 0,125" fill="#0a2860" opacity=".6"/></svg>
  <h2 class="abs">WE CHOOSE US?</h2>
  <p class="abs">At Beacon Advisory, we believe that the a real service offering is one where the client is able to leverage our expertise, our experience and our domain strength to simplify their business processes and enhance the value they add to their stakeholders.</p>
</section>

<footer class="site-footer abs">
  <div class="f-col quick abs" style="left:80px;top:53px;width:168px">
    <h4>QUICK LINKS</h4>
    <ul><li>HOME</li><li>SERVICES</li><li>SOLUTIONS</li><li>RESOURCES</li><li>CAREER</li><li>CONTACT US</li></ul>
  </div>
  <div class="f-col contact abs" style="left:303px;top:53px;width:283px">
    <h4>CONTACT INFORMATION</h4>
    <ul>
      <li><svg width="10" height="14" viewBox="0 0 10 14"><path d="M5 0a5 5 0 0 1 5 5c0 4-5 9-5 9S0 9 0 5a5 5 0 0 1 5-5z" fill="#ddd"/><circle cx="5" cy="5" r="2" fill="#1c1c1c"/></svg><span>Lindenweg 14 4410 Marbach,<br>Northland</span></li>
      <li><svg width="10" height="14" viewBox="0 0 10 14"><path d="M3 0h3v4H4c0 3 1 5 2 6h2v4H5C2 12 0 8 0 5 0 2 1 0 3 0z" fill="#ddd"/></svg><span>+1 (555) 014 2290</span></li>
      <li><svg width="12" height="14" viewBox="0 0 12 14"><rect x="0" y="4" width="12" height="8" fill="#ddd"/><polyline points="0,4 6,9 12,4" fill="none" stroke="#1c1c1c"/></svg><span>info@beaconadvisory.example</span></li>
    </ul>
  </div>
  <div class="f-col newsletter abs" style="left:640px;top:53px;width:242px">
    <h4>NEWSLETTER SIGNUP</h4>
    <p>Please enter your email address below to receive our FREE newsletter</p>
    <div class="email-box">Your Email ID</div>
    <span class="subscribe">SUBSCRIBE</span>
  </div>
  <div class="f-col social abs" style="left:933px;top:53px;width:187px">
    <h4>FOLLOW US</h4>
    <ul>
      <li><i style="background:#3b5a9a"></i>Friendlink</li>
      <li><i style="background:#e3a81b"></i>Workedge</li>
      <li><i style="background:#2aa3e0"></i>Chirper</li>
      <li><i style="background:#19b3c4"></i>Email</li>
    </ul>
  </div>
</footer>
<div class="copyright abs">Copyright @ Beacon Advisory</div>

</body>
</html>
```